Kestrel Table Hour Podcast Episode Cover

I’m looking for a clean, professional, and eye-catching podcast episode cover template for my show, Kestrel Table Hour. Each week, I feature a new guest, so the design must allow me (or my team) to easily swap in a new guest’s photo without needing advanced design skills.

The template should be:

- Drag-and-drop friendly: simple for me to replace the guest’s headshot in Canva, Photoshop, or similar.
- On-brand with the Kestrel Table Hour podcast: professional yet approachable, foodservice industry-focused.
- Bold and attention-grabbing for podcast platforms and social media.

Readable text at small sizes, since covers are often viewed as thumbnails.

Design Elements to Include:

1. Podcast Title: “Kestrel Table Hour” (prominently displayed)
2. Subtitle/Space: Line for guest’s name, professional title, and company name
3. Photo Placeholder: Large, central area where I can easily drag and drop a guest photo
4. Brand Colors: attached
5. Clean, modern fonts (easy to read at thumbnail size)
6. Background graphics or patterns that give a sense of foodservice, leadership, or nationwide reach... but do not overpower the guest photo

Format Requirements:

- Editable source file (PSD, Canva template, or layered AI/INDD)
- JPG/PNG exports for immediate use
- Square format (3000x3000px) for podcast platforms

Style Inspiration:
Think modern podcast covers: bold fonts, clean lines, professional with a touch of energy.

Deliverables:

1. Final episode cover template (editable file)
2. Instructions or guidance on how to swap out guest photos

```html
<!DOCTYPE html>
<html lang="en">
<head>
<meta charset="UTF-8">
<title>Kestrel Table Hour – Episode Cover</title>
<link rel="stylesheet" href="https://fonts.googleapis.com/css2?family=Barlow+Condensed:wght@600;700&family=Montserrat:wght@300;400;600&display=swap">
<style>
  :root {
    --navy: #1b3550;
    --navy-deep: #142a41;
    --gold: #f9b800;
    --white: #fbf9f6;
    --shirt: #e9ecef;
    --vest: #0d0f12;
  }
  html, body {
    margin: 0;
    padding: 0;
    width: 1200px;
    height: 1200px;
    overflow: hidden;
    background: #ffffff;
  }
  .cover {
    position: relative;
    width: 1200px;
    height: 1200px;
    background: var(--navy);
    overflow: hidden;
    font-family: "Montserrat", sans-serif;
  }
  .guest-photo {
    position: absolute;
    left: 810px;
    top: 198px;
    width: 365px;
    height: 1002px;
    border-radius: 180px 180px 0 0;
    background: linear-gradient(180deg, #2a2f36 0%, #d9dde2 32%, #c9ced4 48%, var(--vest) 62%, var(--vest) 100%);
    opacity: 0.95;
  }
  .show-title {
    position: absolute;
    left: 0;
    top: 280px;
    width: 800px;
    text-align: center;
    font-family: "Barlow Condensed", sans-serif;
    font-weight: 700;
    color: var(--white);
    text-transform: uppercase;
    line-height: 1;
  }
  .show-title .line-one {
    display: block;
    font-size: 200px;
    letter-spacing: 2px;
  }
  .show-title .line-two {
    display: block;
    font-size: 168px;
    margin-top: 8px;
    letter-spacing: 2px;
  }
  .guest-info {
    position: absolute;
    left: 76px;
    top: 872px;
    text-transform: uppercase;
  }
  .guest-name {
    margin: 0;
    font-size: 48px;
    font-weight: 600;
    color: var(--gold);
    line-height: 1.05;
  }
  .guest-title {
    margin: 6px 0 0;
    font-size: 22px;
    font-weight: 300;
    letter-spacing: 5px;
    color: var(--white);
  }
  .guest-company {
    margin: 6px 0 0;
    font-size: 28px;
    font-weight: 600;
    letter-spacing: 4px;
    color: var(--white);
  }
  .podcast-label {
    position: absolute;
    left: 330px;
    top: 1080px;
    margin: 0;
    font-size: 60px;
    font-weight: 300;
    letter-spacing: 50px;
    color: var(--white);
  }
</style>
</head>
<body>
  <main class="cover">
    <div class="guest-photo" role="img" aria-label="Guest photo placeholder: smiling server in white shirt and black vest holding a silver tray"></div>

    <h1 class="show-title">
      <span class="line-one">Kestrel</span>
      <span class="line-two">Table Hour</span>
    </h1>

    <section class="guest-info">
      <p class="guest-name">Guest’s Name</p>
      <p class="guest-title">Professional Title</p>
      <p class="guest-company">Company Name</p>
    </section>

    <p class="podcast-label">PODCAST</p>
  </main>
</body>
</html>
```